Redesign of our brintaval.com VPS mini site

We need to a full redesign (modern, fancy and attractive) with a new logo. The site is http://www.brintaval.com/

We are open to any idea / suggestion. Content will not be much more than what is present on the actual web site. We would like to see more filler images inside the page.

Into the attached files I've included all the current web pages
Updates

Project Deadline Extended
Reason: Need more time to make a choice.

Target Market(s)

Internet Hosting

Industry/Entity Type

Internet Service Provider

Logo Text

Quarly BrinTaval

Coding

Coded - Design and coding required

Number of Pages Required

3 page

Font styles to use
Sans Serif

```html
<!DOCTYPE html>
<html lang="en">
<head>
<meta charset="utf-8">
<title>Quarly BrinTaval – Cheap OpenKV Private Servers</title>
<link href="https://fonts.googleapis.com/css2?family=Roboto:wght@300;400;500&display=swap" rel="stylesheet">
<style>
:root{
  --gold:#c8960f;
  --gold-dark:#a97c06;
  --ink:#2b2b2b;
  --text:#555;
  --muted:#8a8a8a;
  --band:#2f2f2f;
  --footer:#333;
  --white:#fff;
  --hero-a:#0e5287;
  --hero-b:#0a3560;
}
*{box-sizing:border-box;margin:0;padding:0}
html,body{width:968px;height:1200px;overflow:hidden}
body{position:relative;font-family:'Roboto',sans-serif;background:var(--white);color:var(--text)}
.topline{position:absolute;left:0;top:0;width:968px;height:3px;background:var(--ink)}
.site-header{position:absolute;left:0;top:3px;width:968px;height:72px}
.brand{position:absolute;left:60px;top:26px;display:flex;align-items:center;gap:7px;font-size:15px;font-weight:500;color:var(--ink);letter-spacing:.3px}
.brand-dot{width:14px;height:14px;border-radius:50%;background:var(--gold)}
.main-nav a{position:absolute;top:32px;font-size:11px;color:var(--ink);text-decoration:none}
.main-nav a.active{color:var(--gold)}
.hero{position:absolute;left:0;top:75px;width:968px;height:351px;background:radial-gradient(ellipse at 60% 40%,var(--hero-a),var(--hero-b))}
.hero-title{position:absolute;left:234px;top:153px;width:500px;height:46px;background:rgba(0,0,0,.22);color:var(--white);font-size:32px;font-weight:400;text-align:center;line-height:46px;letter-spacing:.5px}
.dots{position:absolute;top:314px;left:454px;display:flex;gap:6.5px}
.dots span{width:10px;height:10px;border-radius:50%;background:var(--white)}
.dots span.on{background:var(--gold)}
.welcome{position:absolute;left:70px;top:452px;width:828px;text-align:center}
h2{font-weight:400;color:var(--gold);text-transform:uppercase}
.welcome h2{font-size:18px;margin-bottom:13px}
.welcome p{font-size:11px;line-height:17px;font-weight:300;color:var(--text)}
.features{position:absolute;left:0;top:586px;width:968px;height:284px;background:radial-gradient(ellipse at 20% 50%,#555,var(--band) 55%)}
.features .visual{position:absolute;left:72px;top:18px;width:236px;height:248px;background:linear-gradient(160deg,#3a3a3a,#151515);border-radius:4px}
.features h2{position:absolute;left:362px;top:33px;font-size:18px}
.features .lead{position:absolute;left:364px;top:63px;width:540px;font-size:11px;line-height:18.5px;font-weight:300;color:#ddd}
.ticklist{list-style:none;position:absolute}
.ticklist li{height:24.6px;font-size:10.5px;display:flex;align-items:flex-start;gap:7px}
.ticklist svg{flex:none;margin-top:2px}
.features .ticklist{top:133px;color:#eee}
.offer h2{position:absolute;left:60px;top:900px;font-size:17.5px}
.offer p{position:absolute;left:60px;width:474px;font-size:10.5px;line-height:17px;font-weight:300;color:var(--text)}
.cta{position:absolute;left:60px;top:1042px;display:flex;align-items:center;gap:17px}
.cta span{font-size:12px;color:var(--ink);font-weight:500;width:128px}
.cta a{display:block;width:108px;height:28px;background:var(--gold-dark);color:var(--white);font-size:12px;font-weight:500;text-align:center;line-height:28px;text-decoration:none}
.templates h3{position:absolute;left:570px;top:902px;font-size:12px;font-weight:500;color:var(--gold)}
.templates .ticklist{top:933px;color:var(--ink)}
.site-footer{position:absolute;left:0;top:1110px;width:968px;height:90px;background:linear-gradient(#333 60%,#4a4a4a)}
.foot-nav a{position:absolute;top:24px;font-size:10px;color:#ccc;text-decoration:none}
.copy{position:absolute;left:60px;top:51px;font-size:9px;color:#999;font-weight:300}
.social{position:absolute;top:34px;left:795px;display:flex;gap:6px}
.social span{width:24px;height:24px;border-radius:50%;background:var(--gold)}
</style>
</head>
<body>
<div class="topline"></div>
<header class="site-header">
  <div class="brand"><span class="brand-dot"></span>Quarly BrinTaval</div>
  <nav class="main-nav">
    <a class="active" href="#" style="left:678px">HOME</a>
    <a href="#" style="left:737px">DDOS</a>
    <a href="#" style="left:794px">FAQ</a>
    <a href="#" style="left:842px">CONTACT US</a>
  </nav>
</header>

<section class="hero" role="img" aria-label="Row of black tower servers standing on a blue grid floor">
  <h1 class="hero-title">Cheap OpenKV Private Servers</h1>
  <div class="dots"><span class="on"></span><span></span><span></span><span></span></div>
</section>

<section class="welcome">
  <h2>Welcome to our website</h2>
  <p>OpenKV is container-based virtualization for Kernix. OpenKV creates multiple secure, isolated Kernix containers (otherwise known as VEs or VPSs) on a single physical server enabling better server utilization.One of the main criticisms about OpenKV is that it's easy for providers to overcommit resources (aka "Overselling"), but when it's done right the virtualization (technically acontext separation) offered by OpenKV offers near bare metal performances.</p>
</section>

<section class="features">
  <div class="visual" role="img" aria-label="Server rack cabinet full of drive bays"></div>
  <h2>BrinTaval VPS Features</h2>
  <p class="lead">BrinTaval was born as a brand to promote VPS services with a lot of overcommitted resources. We keep servers running at 70-100% usage all the time while keeping performances under control balancing containers over different nodes when required..</p>
  <ul class="ticklist" style="left:364px">
    <li><svg width="9" height="9" viewBox="0 0 10 10"><path d="M1 5.5l2.5 2.5L9 2" fill="none" stroke="#c8960f" stroke-width="2"/></svg>4 CPU Cores</li>
    <li><svg width="9" height="9" viewBox="0 0 10 10"><path d="M1 5.5l2.5 2.5L9 2" fill="none" stroke="#c8960f" stroke-width="2"/></svg>4 GB RAM</li>
    <li><svg width="9" height="9" viewBox="0 0 10 10"><path d="M1 5.5l2.5 2.5L9 2" fill="none" stroke="#c8960f" stroke-width="2"/></svg>40 GB DISK</li>
    <li><svg width="9" height="9" viewBox="0 0 10 10"><path d="M1 5.5l2.5 2.5L9 2" fill="none" stroke="#c8960f" stroke-width="2"/></svg>2000 GB Traffic</li>
    <li><svg width="9" height="9" viewBox="0 0 10 10"><path d="M1 5.5l2.5 2.5L9 2" fill="none" stroke="#c8960f" stroke-width="2"/></svg>Kernix Operating System</li>
  </ul>
  <ul class="ticklist" style="left:526px">
    <li><svg width="9" height="9" viewBox="0 0 10 10"><path d="M1 5.5l2.5 2.5L9 2" fill="none" stroke="#c8960f" stroke-width="2"/></svg>TUN / TAP / PPP / FUSE</li>
    <li><svg width="9" height="9" viewBox="0 0 10 10"><path d="M1 5.5l2.5 2.5L9 2" fill="none" stroke="#c8960f" stroke-width="2"/></svg>1 IPv4, 4 IPv6</li>
    <li><svg width="9" height="9" viewBox="0 0 10 10"><path d="M1 5.5l2.5 2.5L9 2" fill="none" stroke="#c8960f" stroke-width="2"/></svg>Shared Gigabit speed</li>
    <li><svg width="9" height="9" viewBox="0 0 10 10"><path d="M1 5.5l2.5 2.5L9 2" fill="none" stroke="#c8960f" stroke-width="2"/></svg>NodeDeck Control Panel</li>
    <li><svg width="9" height="9" viewBox="0 0 10 10"><path d="M1 5.5l2.5 2.5L9 2" fill="none" stroke="#c8960f" stroke-width="2"/></svg>Location: Milan, Italy</li>
  </ul>
  <ul class="ticklist" style="left:707px">
    <li><svg width="9" height="9" viewBox="0 0 10 10"><path d="M1 5.5l2.5 2.5L9 2" fill="none" stroke="#c8960f" stroke-width="2"/></svg>Test IP 192.0.2.10</li>
    <li><svg width="9" height="9" viewBox="0 0 10 10"><path d="M1 5.5l2.5 2.5L9 2" fill="none" stroke="#c8960f" stroke-width="2"/></svg>Unmanaged service</li>
    <li><svg width="9" height="9" viewBox="0 0 10 10"><path d="M1 5.5l2.5 2.5L9 2" fill="none" stroke="#c8960f" stroke-width="2"/></svg>No refund</li>
  </ul>
</section>

<section class="offer">
  <h2>Only for GBP £ 5 monthly</h2>
  <p style="top:931px">We highly recommend to buy also the DDOS protected IP. It's only £ 5.00 more per month and can protect from some of the most common attack fo up to 10Gbps and 1 Million packets per second.</p>
  <p style="top:973px">No long term commitment, when you don't like the service or don't need it anymore, just ask for a cancellation at the end of the month. Please remember that we don't offer refunds, so if you aren't sure just don't buy this product and look at our regular openkv plans :-)</p>
  <div class="cta"><span>Are you ready to start?</span><a href="#">ORDER NOW</a></div>
</section>

<section class="templates">
  <h3>AVAILABLE TEMPLATES</h3>
  <ul class="ticklist" style="left:570px">
    <li><svg width="9" height="9" viewBox="0 0 10 10"><path d="M1 5.5l2.5 2.5L9 2" fill="none" stroke="#c8960f" stroke-width="2"/></svg>CedarOS 5 32/64 bit</li>
    <li><svg width="9" height="9" viewBox="0 0 10 10"><path d="M1 5.5l2.5 2.5L9 2" fill="none" stroke="#c8960f" stroke-width="2"/></svg>CedarOS 6 32/64 bit</li>
    <li><svg width="9" height="9" viewBox="0 0 10 10"><path d="M1 5.5l2.5 2.5L9 2" fill="none" stroke="#c8960f" stroke-width="2"/></svg>Delvian 6 32/64 bit</li>
    <li><svg width="9" height="9" viewBox="0 0 10 10"><path d="M1 5.5l2.5 2.5L9 2" fill="none" stroke="#c8960f" stroke-width="2"/></svg>Ubirra 10.04 32/64 bit</li>
    <li><svg width="9" height="9" viewBox="0 0 10 10"><path d="M1 5.5l2.5 2.5L9 2" fill="none" stroke="#c8960f" stroke-width="2"/></svg>Ubirra 11.10 32/64 bit</li>
    <li><svg width="9" height="9" viewBox="0 0 10 10"><path d="M1 5.5l2.5 2.5L9 2" fill="none" stroke="#c8960f" stroke-width="2"/></svg>Ubirra 12.04 32/64 bit</li>
  </ul>
  <ul class="ticklist" style="left:764px">
    <li><svg width="9" height="9" viewBox="0 0 10 10"><path d="M1 5.5l2.5 2.5L9 2" fill="none" stroke="#c8960f" stroke-width="2"/></svg>Ubirra 12.10 32/64 bit</li>
    <li><svg width="9" height="9" viewBox="0 0 10 10"><path d="M1 5.5l2.5 2.5L9 2" fill="none" stroke="#c8960f" stroke-width="2"/></svg>BoxHostly - CedarOS 5</li>
    <li><svg width="9" height="9" viewBox="0 0 10 10"><path d="M1 5.5l2.5 2.5L9 2" fill="none" stroke="#c8960f" stroke-width="2"/></svg>ReadyKit Kernix PressKit</li>
    <li><svg width="9" height="9" viewBox="0 0 10 10"><path d="M1 5.5l2.5 2.5L9 2" fill="none" stroke="#c8960f" stroke-width="2"/></svg>ReadyKit Kernix ForumBB</li>
  </ul>
</section>

<footer class="site-footer">
  <nav class="foot-nav">
    <a href="#" style="left:60px">HOME</a>
    <a href="#" style="left:115px">DDOS</a>
    <a href="#" style="left:168px">FAQ</a>
    <a href="#" style="left:214px">CONTACT US</a>
  </nav>
  <p class="copy">Copyright © 2015. Company Name. All Right Reserved. Privacy Policy</p>
  <div class="social"><span></span><span></span><span></span><span></span></div>
</footer>
</body>
</html>
```